Mobile grocery convenience store app

PantryVan is a mobile grocery store. Customers should be able to request the grocery bus to their home address. See where the bus is with map and estimated time. Put multiple people requests in order they request. Give an 15 min -20 min per stop for customers to come aboard bus and shops/pay for for their grocery. Must have log in for bus driver/clerk to sign in and see get directions to next address in que and info they would need. Such as contact for customer should driver get lost. Similar to zippa and Ridora. Special instructions for handicap so driver can bring items to door. Products we sale should be able to be added or changed easily by manager or sign in.
Updates

Problem starting design contest. Was never supposed to be 6 days. Thanks

Industry/Entity Type

Grocery

Font styles to use
Sans Serif

Colors
0255a3
fee18a
fece3e

Requirements
Must have
• Colors match as close to logo colors

```html
<!DOCTYPE html>
<html lang="en">
<head>
<meta charset="utf-8">
<title>PantryVan – Next Stop</title>
<link rel="stylesheet" href="https://fonts.googleapis.com/css2?family=Red+Hat+Display:wght@400;500;700;900&display=swap">
<style>
  :root {
    --brand-blue: #0255a3;
    --brand-yellow: #fece3e;
    --brand-yellow-soft: #fee18a;
    --map-base: #e8e9ec;
    --map-green: #cfe6c4;
    --map-road: #f7f7f8;
    --text-body: #666a70;
    --text-strong: #55595e;
    --card-bg: #ffffff;
    --white: #ffffff;
  }
  * { box-sizing: border-box; margin: 0; padding: 0; }
  html, body { width: 675px; height: 1200px; overflow: hidden; background: var(--white); }
  body { font-family: "Red Hat Display", Arial, sans-serif; position: relative; }

  .status-bar {
    position: absolute; left: 0; top: 0; width: 675px; height: 52px;
    background: var(--brand-blue); color: var(--white);
    display: flex; align-items: center; justify-content: space-between;
    padding: 0 16px 0 14px; z-index: 3;
  }
  .status-time { font-size: 18px; font-weight: 500; letter-spacing: 0.3px; }
  .status-icons { display: flex; gap: 8px; align-items: center; }

  .map-area {
    position: absolute; left: 0; top: 52px; width: 675px; height: 1148px;
    background:
      linear-gradient(180deg, rgba(255,255,255,0) 0%, rgba(255,255,255,0) 82%, rgba(255,255,255,1) 100%),
      radial-gradient(ellipse 170px 130px at 420px 220px, rgba(190,225,175,0.75) 0%, rgba(190,225,175,0) 100%),
      radial-gradient(ellipse 110px 120px at 250px 320px, rgba(190,225,175,0.6) 0%, rgba(190,225,175,0) 100%),
      radial-gradient(ellipse 140px 90px at 620px 250px, rgba(205,230,195,0.5) 0%, rgba(205,230,195,0) 100%),
      linear-gradient(160deg, #ececef 0%, var(--map-base) 50%, #e3e5e8 100%);
  }
  .map-pin { position: absolute; width: 56px; height: 76px; z-index: 1; }
  .map-pin--current { left: 147px; top: 231px; }
  .map-pin--next { left: 332px; top: 510px; }

  .stop-card {
    position: absolute; left: 35px; top: 601px; width: 601px; height: 527px;
    background: var(--card-bg); border-radius: 8px;
    box-shadow: 0 14px 40px rgba(0,0,0,0.18);
    padding: 52px 40px 0 52px; z-index: 2;
  }
  .stop-eta { display: flex; align-items: center; gap: 20px; }
  .eta-icon { width: 58px; height: 58px; flex: none; }
  .eta-value { font-size: 33px; font-weight: 700; color: var(--brand-blue); line-height: 1; letter-spacing: -0.5px; }
  .eta-label { font-size: 20px; font-weight: 400; color: #222; margin-top: 4px; }
  .stop-rating { display: flex; gap: 2px; margin-top: 20px; }
  .stop-rating svg { width: 20px; height: 20px; }
  .stop-description { margin-top: 30px; font-size: 19.5px; line-height: 34px; color: var(--text-body); white-space: nowrap; }
  .address-label { margin-top: 14px; font-size: 19.5px; font-weight: 700; color: var(--text-strong); letter-spacing: 0.5px; }
  .address-text { margin-top: 2px; font-size: 19.5px; line-height: 34px; color: var(--text-body); white-space: nowrap; }
  .direction-button {
    display: inline-flex; align-items: center; justify-content: center;
    margin-top: 22px; width: 274px; height: 58px; border-radius: 29px; border: none;
    background: var(--brand-yellow); color: var(--white);
    font-family: "Red Hat Display", Arial, sans-serif;
    font-size: 21px; font-weight: 900; letter-spacing: 2px;
  }
</style>
</head>
<body>
  <header class="status-bar">
    <span class="status-time">9:41</span>
    <span class="status-icons">
      <svg width="24" height="16" viewBox="0 0 24 16" fill="#fff"><rect x="0" y="11" width="4" height="5" rx="1"/><rect x="6" y="8" width="4" height="8" rx="1"/><rect x="12" y="4" width="4" height="12" rx="1"/><rect x="18" y="0" width="4" height="16" rx="1"/></svg>
      <svg width="22" height="16" viewBox="0 0 22 16" fill="none" stroke="#fff" stroke-width="2.4" stroke-linecap="round"><path d="M2 5.5a13 13 0 0 1 18 0"/><path d="M5.5 9a8 8 0 0 1 11 0"/><circle cx="11" cy="13" r="1.6" fill="#fff" stroke="none"/></svg>
      <svg width="34" height="17" viewBox="0 0 34 17"><rect x="1" y="1" width="28" height="15" rx="4" fill="none" stroke="#fff" stroke-width="2"/><rect x="4" y="4" width="22" height="9" rx="2" fill="#fff"/><rect x="31" y="5.5" width="2.5" height="6" rx="1" fill="#fff"/></svg>
    </span>
  </header>

  <main>
    <div class="map-area" role="img" aria-label="Street map of the neighbourhood with parks and roads, showing the bus route and upcoming stops"></div>

    <svg class="map-pin map-pin--current" viewBox="0 0 56 76" aria-hidden="true"><path d="M28 0C12.5 0 0 12.3 0 27.5 0 47 28 76 28 76s28-29 28-48.5C56 12.3 43.5 0 28 0z" fill="var(--brand-blue)"/><circle cx="28" cy="27" r="12" fill="#fff"/></svg>
    <svg class="map-pin map-pin--next" viewBox="0 0 56 76" aria-hidden="true"><path d="M28 0C12.5 0 0 12.3 0 27.5 0 47 28 76 28 76s28-29 28-48.5C56 12.3 43.5 0 28 0z" fill="var(--brand-blue)"/><circle cx="28" cy="27" r="12" fill="#fff"/></svg>

    <section class="stop-card">
      <div class="stop-eta">
        <svg class="eta-icon" viewBox="0 0 58 58" fill="none" stroke="var(--brand-blue)" stroke-width="3.5" stroke-linecap="round"><circle cx="29" cy="29" r="26.5"/><path d="M29 12v17l9 10"/><path d="M29 5.5v3M29 49.5v3M5.5 29h3M49.5 29h3" stroke-width="2.5"/></svg>
        <div>
          <div class="eta-value">15 min -20</div>
          <div class="eta-label">min per stop</div>
        </div>
      </div>
      <div class="stop-rating" aria-label="Rated 4 of 5">
        <svg viewBox="0 0 24 24"><path d="M12 2l3 6.5 7 .8-5.2 4.8 1.4 7L12 17.6 5.8 21.1l1.4-7L2 9.3l7-.8z" fill="var(--brand-yellow)"/></svg>
        <svg viewBox="0 0 24 24"><path d="M12 2l3 6.5 7 .8-5.2 4.8 1.4 7L12 17.6 5.8 21.1l1.4-7L2 9.3l7-.8z" fill="var(--brand-yellow)"/></svg>
        <svg viewBox="0 0 24 24"><path d="M12 2l3 6.5 7 .8-5.2 4.8 1.4 7L12 17.6 5.8 21.1l1.4-7L2 9.3l7-.8z" fill="var(--brand-yellow)"/></svg>
        <svg viewBox="0 0 24 24"><path d="M12 2l3 6.5 7 .8-5.2 4.8 1.4 7L12 17.6 5.8 21.1l1.4-7L2 9.3l7-.8z" fill="var(--brand-yellow)"/></svg>
        <svg viewBox="0 0 24 24"><path d="M12 2l3 6.5 7 .8-5.2 4.8 1.4 7L12 17.6 5.8 21.1l1.4-7L2 9.3l7-.8z" fill="none" stroke="var(--brand-yellow)" stroke-width="1.3"/></svg>
      </div>
      <p class="stop-description">Ipsum is simply dummy text of the printing and typeset-<br>ting industry. Lorem Ipsum has been the industry's stan-<br>dard dummy text ever since the</p>
      <h3 class="address-label">ADDRESS :</h3>
      <p class="address-text">Abdc Street city #12345 Ipsum is simply dummy text of<br>the printing and typesetting industry</p>
      <button class="direction-button" type="button">GET DIRECTION</button>
    </section>
  </main>
</body>
</html>
```